Velbrant End of Life Postcard

We want the design of the postcard (size of card is US 6"x11" Horizontal) to jump out. We want people to understand the urgency of the message we are sending. <br/><br/>This postcard will be sent to several thousand businesses expressing the urgency they upgrade from a few platforms that Velbrant is ending support for in January. See attached info sheet for info. Ignore the image in this, it was used internally to drive ideas only. <br/><br/>I have attached examples of our previous mailers too so you can see the style and where the address and stamp need to go.

Target Market(s)

Small & Medium Business with under 2,000 employees.

Industry/Entity Type

Information Technology

Font styles to use
Sans Serif
Other font styles liked:
• Open-Sans

Colors
0355a3

Requirements
Must have
• Great design. Respect for white-space and clean lines. Eye catching and not look like a template was used.
Should not have
• Please do not use the 'gold/brown' color in our StyleGuide

```html
<!DOCTYPE html>
<html lang="en">
<head>
<meta charset="utf-8">
<title>Velbrant End of Life Postcard</title>
<link rel="stylesheet" href="https://fonts.googleapis.com/css2?family=Open+Sans:wght@400;600;700;800&family=Arimo:wght@400&display=swap">
<style>
  :root{
    --brand-blue:#04559a;
    --accent-cyan:#1cb0ec;
    --band-dark:#231f20;
    --fold-grey:#8f8f91;
    --paper:#ffffff;
    --ink:#111111;
    --backdrop:#6d6d6d;
  }
  *{margin:0;padding:0;box-sizing:border-box}
  html,body{width:1200px;height:727px;overflow:hidden;background:var(--backdrop)}
  .postcard{position:absolute;left:92px;top:87px;width:1017px;height:554px;background:var(--paper);font-family:"Open Sans",sans-serif}
  .message-panel{position:absolute;left:0;top:0;width:538px;height:554px;background:var(--brand-blue);color:#fff}
  .headline{position:absolute;left:49px;top:34px;font-size:30px;font-weight:800;letter-spacing:.3px;white-space:nowrap}
  .intro{position:absolute;left:49px;top:77px;width:470px;font-size:14.2px;line-height:18px}
  .intro strong{font-weight:700}
  .subhead{position:absolute;left:49px;top:151px;font-size:16.4px;font-weight:800;white-space:nowrap}
  .risk-copy{position:absolute;left:49px;top:185px;width:480px;font-size:14.2px;line-height:18px}
  .fact-band{position:absolute;left:0;top:265px;width:562px;height:151px;background:var(--band-dark);color:#fff;padding:12px 0 0 46px}
  .fact-band ul{list-style:none}
  .fact-band li{position:relative;padding-left:13px;font-size:14.4px;line-height:17px;margin-bottom:5.3px}
  .fact-band li::before{content:"";position:absolute;left:-7px;top:4px;width:8px;height:8px;border-radius:50%;background:var(--accent-cyan)}
  .fact-band .highlight{color:var(--accent-cyan);font-weight:700}
  .fold{position:absolute;left:538px;top:416px}
  .deadline{position:absolute;left:55px;top:436px;font-size:27px;font-weight:700;white-space:nowrap}
  .call-to-action{position:absolute;left:55px;top:474px;font-size:21.5px;font-weight:700;line-height:26px}
  .call-to-action .link{color:var(--accent-cyan)}
  .call-to-action .phone{color:var(--accent-cyan);font-weight:600}
  .return-block{position:absolute;left:582px;top:38px}
  .sender-name{display:flex;align-items:center;gap:7px;font-size:27px;font-weight:800;color:var(--ink);letter-spacing:-.3px}
  .sender-name .dot{width:12px;height:12px;border-radius:50%;background:var(--brand-blue)}
  .sender-address{margin:14px 0 0 9px;font-family:"Arimo",sans-serif;font-size:12px;line-height:15.5px;color:var(--ink)}
  .postage-indicia{position:absolute;left:855px;top:45px;width:119px;height:58px;border:1.3px solid var(--ink);font-family:"Arimo",sans-serif;font-size:8.6px;line-height:10.8px;text-align:center;padding-top:6px;color:var(--ink)}
</style>
</head>
<body>
<div class="postcard">
  <section class="message-panel">
    <h1 class="headline">YOU CAN’T AFFORD TO WAIT!</h1>
    <p class="intro">We have 95+ full-time employees ready to assist your organization in the upgrade and ensure you are secure before it’s too late.<br><strong>No long-term contracts. Affordable rates.</strong></p>
    <h2 class="subhead">What happens if you don’t upgrade by the deadline?</h2>
    <p class="risk-copy">You will be a target almost immediately, hands down.<br>It is anticipated that within days of the deadline ransomware<br>will target the masses and spread quickly costing billions of dollars in damages.</p>
    <p class="deadline">DEADLINE: January 14th, 2020</p>
    <p class="call-to-action">Visit <span class="link">www.EndSupport2020.com</span> for more details<br>or call us at <span class="phone">(800) 555-0147</span></p>
  </section>
  <section class="fact-band">
    <ul>
      <li>43% of desktops are still running Velbrant Desk 7</li>
      <li>63% of Velbrant Servers are still running Velbrant Server 2008 or older</li>
      <li>Average cost of each ransomware incident is in excess of <span class="highlight">$713,000</span></li>
      <li>Small &amp; Medium sized business are the target</li>
      <li>Recovering files from backup and restoring encrypted systems is often easier said than done</li>
    </ul>
  </section>
  <svg class="fold" width="24" height="22" viewBox="0 0 24 22"><polygon points="0,0 24,0 0,22" fill="var(--fold-grey)"/></svg>
  <section class="return-block">
    <div class="sender-name"><span class="dot"></span>Northgate IT</div>
    <p class="sender-address">275 N. Alder Ave<br>Suite 310<br>Fairhaven, WA 98120</p>
  </section>
  <div class="postage-indicia">Presorted Standard<br>US Postage Paid<br>Lakemont, WA<br>Permit No. 482</div>
</div>
</body>
</html>
```